Redesign der Webseite www.velmor-gmbh.de
Zielgruppe
Kunden im Ausland (Maschinen für die Getränkeindustrie) siehe Webseite.
Unterschiedliche Bereiche visuell abbilden.
Im modernem Outfit gestalten.
Nähere Infos unter:
E-Mail: k.brandler@velmor-gmbh.de
Tel.: +49-6253-4172-0
Aufgabenstellung
ein komplett NEUE Seite esrtellen auf der grundlage von vorhandenen Daten
Mehrsprachig mit schwerpunkt Russisch etc.

```html
<!DOCTYPE html>
<html lang="de">
<head>
<meta charset="utf-8">
<title>VELMOR GmbH – Abfüllanlagen</title>
<link rel="stylesheet" href="https://fonts.googleapis.com/css2?family=Gelasio:ital,wght@0,400;0,700;1,400;1,700&display=swap">
<style>
:root{
  --red:#e0101a;
  --ink:#1e1e1e;
  --card:#f7f7f7;
  --line:#cfcfcf;
}
*{margin:0;padding:0;box-sizing:border-box}
html,body{width:1200px;height:960px;overflow:hidden}
body{position:relative;background:linear-gradient(#fafafa 0,#ececec 150px,#f4f4f4 420px,#ededed 960px);font-family:"Gelasio",Georgia,serif;color:var(--ink)}
.abs{position:absolute}
.brand{left:63px;top:35px;width:145px;font-size:32px;font-weight:700;color:var(--red);letter-spacing:0;line-height:1;white-space:nowrap}
.tagline{left:219px;top:38px;border-left:2px solid var(--red);padding-left:9px;font-size:11px;font-style:italic;line-height:15px;color:var(--ink);white-space:nowrap}
.topmeta{left:905px;top:28px;font-size:11px;font-style:italic;display:flex;gap:6px;align-items:center}
.topmeta .sep{color:var(--red)}
.flag{width:16px;height:11px;display:inline-block;margin-left:5px}
.flag.de{background:linear-gradient(#111 0 33%,#d00 33% 66%,#f5c400 66%)}
.flag.ru{background:linear-gradient(#fff 0 33%,#1d3fa8 33% 66%,#d52b1e 66%);outline:1px solid #ccc}
.flag.tr{background:#e30a17;border-radius:2px}
.mainnav{left:58px;top:105px;display:flex;font-size:15px;font-style:italic;text-transform:uppercase}
.mainnav a{color:var(--ink);text-decoration:none}
.mainnav .sep{color:var(--red);margin:0 8px}
.search{left:930px;top:105px;width:180px;height:22px;border-bottom:1px solid #c8c8c8;font-size:10px;font-style:italic;color:#888;padding:5px 4px;text-transform:uppercase}
.search-icon{left:1115px;top:100px}
.band{left:0;top:140px;width:1200px;height:12px;background:linear-gradient(#e2e2e2,rgba(240,240,240,0))}
.hero-img{left:68px;top:177px;width:372px;height:251px;background:linear-gradient(135deg,#5b6f88 0,#c9cfd8 35%,#8f9aa8 55%,#d8dde4 75%,#4d5f7a 100%);border:3px solid #fff;box-shadow:0 0 4px rgba(0,0,0,.3)}
.pager{left:342px;top:423px;font-size:11px;font-style:italic}
.pager span{color:var(--red);margin:0 2px}
.pager .on{background:#ddd;padding:0 2px}
.hero-text{left:477px;top:207px;width:485px}
.hero-title{display:inline;background:var(--red);color:#fff;font-size:15px;font-weight:700;font-style:italic;line-height:19px;padding:0 3px;box-decoration-break:clone;-webkit-box-decoration-break:clone}
.hero-body{margin-top:5px;font-size:13px;font-style:italic;line-height:16px;text-align:justify}
.cards{left:57px;top:465px;width:1093px;display:flex;gap:11px}
.card{width:265px;height:113px;background:var(--card);box-shadow:0 0 3px rgba(0,0,0,.15);display:flex;align-items:center;padding:0 8px}
.card-img{width:105px;height:100px;background:linear-gradient(160deg,#3f4e60,#a9b3bf 45%,#dfe3e8 60%,#66778b)}
.card-arrow{color:var(--red);font-size:14px;margin:0 8px}
.card-text{font-size:11px;font-style:italic;line-height:13px;width:118px}
.card-text b{display:block;font-size:13px;font-style:normal;margin-bottom:1px}
.news-label{left:57px;top:596px;background:var(--red);color:#fff;font-size:13px;font-weight:700;font-style:italic;padding:1px 5px}
.news-rule{left:57px;top:618px;width:1096px;height:1px;background:var(--line)}
.news-main{left:57px;top:630px;width:1096px;height:135px;background:#fff;box-shadow:0 0 3px rgba(0,0,0,.1)}
.news-img{left:63px;top:635px;width:369px;height:122px;background:linear-gradient(90deg,#e9e3d6 0,#f4f0e8 30%,#f3f3f3 60%,#e6efd8 100%)}
.news-head{left:444px;top:638px;width:706px;display:flex;justify-content:space-between;align-items:center}
.tag{background:var(--red);color:#fff;font-size:10px;font-style:italic;padding:1px 3px}
.date{font-size:11px;font-style:italic}
.date span{color:var(--red)}
.news-body{left:444px;top:657px;width:706px;font-size:10px;line-height:12.5px}
.news-body p+p{margin-top:6px}
.contact{display:grid;grid-template-columns:90px 1fr;margin-top:7px}
.row{left:57px;width:1096px;height:24px;background:#fff;box-shadow:0 0 2px rgba(0,0,0,.15);display:flex;align-items:center;font-size:10px;white-space:nowrap;overflow:hidden;gap:6px}
.row .tag{height:17px;line-height:15px}
.row .sep{color:var(--red)}
.footer-rule{left:0;top:912px;width:1200px;height:1px;background:linear-gradient(90deg,transparent,#d0d0d0 20%,#d0d0d0 80%,transparent)}
.footer{top:929px;font-size:11px;font-style:italic;text-transform:uppercase}
.footer .sep{color:var(--red);margin:0 4px}
</style>
</head>
<body>
<header>
  <div class="abs brand">VELMOR</div>
  <div class="abs tagline">Eine gut geplante Investition heute<br>garantiert ein erfolgreiches Geschäft morgen</div>
  <div class="abs topmeta">KONTAKT <span class="sep">|</span> SERVICE <span class="sep">|</span> SPRACHE: <i class="flag de"></i><i class="flag ru"></i><i class="flag tr"></i></div>
  <nav class="abs mainnav">
    <a href="#">News</a><span class="sep">|</span><a href="#">Unternehmen</a><span class="sep">|</span><a href="#">Produkte</a><span class="sep">|</span><a href="#">Unsere Partner</a><span class="sep">|</span><a href="#">Referenzen</a><span class="sep">|</span><a href="#">Downloads</a>
  </nav>
  <div class="abs search">Suchen...</div>
  <svg class="abs search-icon" width="24" height="26" viewBox="0 0 24 26"><circle cx="14" cy="10" r="7" fill="#bfe3f5" stroke="#4a90b8" stroke-width="2"/><line x1="9" y1="15" x2="2" y2="23" stroke="#555" stroke-width="3" stroke-linecap="round"/></svg>
  <div class="abs band"></div>
</header>

<section>
  <div class="abs hero-img" role="img" aria-label="Foto einer Abfüllanlage mit Edelstahlbehältern"></div>
  <div class="abs pager"><span class="on">1</span>|<span>2</span>|<span>3</span>|<span>4</span>|<span>5</span>|<span>6</span></div>
  <div class="abs hero-text">
    <h1 class="hero-title">Abfüllanlagen für Alkohol und<br>alkoholfreie Getränke</h1>
    <p class="hero-body">Die VELMOR GmbH liefert verschiedene Typen von Anlagen zum Abfüllen alkoholischer und alkoholfreier Getränke.<br>Alle Elemente der Anlage, einschließlich der Förderbänder und der Aufgabentische, werden zum Test der Funktionsfähigkeit im Werk in der Reihenfolge montiert in der die Produktion erfolgen soll. Auf Wunsch kann der Kunde an diesem Testlauf teilnehmen.</p>
  </div>
</section>

<section class="abs cards">
  <div class="card"><div class="card-img" role="img" aria-label="Foto einer Abfüllanlage"></div><span class="card-arrow">&gt;</span><div class="card-text"><b>Abfüllanlagen</b>Die VELMOR GmbH liefert verschiedene Typen</div></div>
  <div class="card"><div class="card-img" role="img" aria-label="Foto einer Abfüllanlage"></div><span class="card-arrow">&gt;</span><div class="card-text"><b>Abfüllanlagen</b>Die VELMOR GmbH liefert verschiedene Typen</div></div>
  <div class="card"><div class="card-img" role="img" aria-label="Foto einer Abfüllanlage"></div><span class="card-arrow">&gt;</span><div class="card-text"><b>Abfüllanlagen</b>Die VELMOR GmbH liefert verschiedene Typen</div></div>
  <div class="card"><div class="card-img" role="img" aria-label="Foto einer Abfüllanlage"></div><span class="card-arrow">&gt;</span><div class="card-text"><b>Abfüllanlagen</b>Die VELMOR GmbH liefert verschiedene Typen</div></div>
</section>

<section>
  <h2 class="abs news-label">Neuigkeiten:</h2>
  <div class="abs news-rule"></div>
  <div class="abs news-main"></div>
  <div class="abs news-img" role="img" aria-label="Messeplakat mit Apfel und Messedaten"></div>
  <div class="abs news-head"><span class="tag">Die VELMOR GmbH lädet ein!</span><span class="date">2010<span>|</span>02<span>|</span>08</span></div>
  <div class="abs news-body">
    <p>Besuchen Sie die Internationale Messe VINOTEXA 2010, die in der Zeit vom dem 08.02 bis 12.02.2010 im MZ „ORBITA“ Moskau, Uferstraße 27. Haltestelle PARKOWAJA (Bahnhof Zentr)</p>
    <p>Wir werden uns freuen, Sie persönlich an unserem Stand 82B70 Gebäude 8 Halle 2 begrüßen zu dürfen. Sie bekommen jegliche fachliche Beratung zur all unseren Maschinen und Anlagen, sowie Abfülltechnologien und Optimierung der technologischen Abläufe und Programmanwendung.</p>
    <div class="contact"><span>Unsere Kontakte:</span><span>+49-6253-4172-0 Zentralbüro in Talbach/Deutschland<br>+ 7 900 123 45 67 - Geschäftsführer Herr Markus Heller</span></div>
  </div>
  <div class="abs row" style="top:765px"><span class="tag">Die VELMOR GmbH lädet ein!</span><span class="date">2010<span>|</span>02<span>|</span>08</span><span class="sep">||</span>Besuchen Sie die Internationale Messe VINOTEXA 2010, die in der Zeit vom dem 08.02 bis 12.02.2010 im MZ „ORBITA“ Moskau, Uferstraße 27. Haltestelle...</div>
  <div class="abs row" style="top:795px"><span class="tag">Die VELMOR GmbH lädet ein!</span><span class="date">2010<span>|</span>02<span>|</span>08</span><span class="sep">||</span>Besuchen Sie die Internationale Messe VINOTEXA 2010, die in der Zeit vom dem 08.02 bis 12.02.2010 im MZ „ORBITA“ Moskau, Uferstraße 27. Haltestelle...</div>
  <div class="abs row" style="top:825px"><span class="tag">Die VELMOR GmbH lädet ein!</span><span class="date">2010<span>|</span>02<span>|</span>08</span><span class="sep">||</span>Besuchen Sie die Internationale Messe VINOTEXA 2010, die in der Zeit vom dem 08.02 bis 12.02.2010 im MZ „ORBITA“ Moskau, Uferstraße 27. Haltestelle...</div>
</section>

<footer>
  <div class="abs footer-rule"></div>
  <div class="abs footer" style="left:66px">© 2010 <span class="sep">|</span> VELMOR GMBH</div>
  <div class="abs footer" style="left:353px">News<span class="sep">|</span>Unternehmen<span class="sep">|</span>Produkte<span class="sep">|</span>Unsere Partner<span class="sep">|</span>Referenzen<span class="sep">|</span>Downloads</div>
  <div class="abs footer" style="left:1030px">AGB<span class="sep">|</span>Impressum</div>
</footer>
</body>
</html>
```